Flyer Design Project

Our company focuses on selling Consumer products like home furniture, home decor, electronics and accessories by public auction. We need a flyer design that will showcase these products with pictures and text. Illustration and desciption on the flyer is always genetic and never changes, The flyer design should be simple and straight forward with limited graphic design and instead focus on product description and emphasise on words Public Auction, and the word AUCTION being the main heading on the flyer. Multilpe colours are prefered.

Target Market(s)

Age group between 30-65 lmajority living in rural, homeowners and looking for a great quality product at an economical price

Industry/Entity Type

Graphic Design

Requirements
Must have
• The flyer should be tri-fold 11x17 inches in size fron and back.
Nice to have
• To show consumers that they have an opportunity to save money by attending our auctions.
Should not have
• The flyer design should not look too corporate or sophisticated. Simple approach to target consumers since most of them live in rural areas.

```html
<!DOCTYPE html>
<html lang="en">
<head>
<meta charset="utf-8">
<title>Partial Listing – Back Page</title>
<link rel="stylesheet" href="https://fonts.googleapis.com/css2?family=Bebas+Neue&family=Alfa+Slab+One&family=Arvo:wght@700&family=PT+Sans:ital,wght@0,400;0,700;1,400;1,700&display=swap">
<style>
  :root{
    --page-bg:#ece7df;
    --ink:#0d1114;
    --white:#ffffff;
    --red:#d8251e;
    --red-deep:#b0160f;
    --yellow:#fbc934;
    --orange:#f3a421;
    --panel-text:#2a1d08;
  }
  *{box-sizing:border-box;margin:0;padding:0}
  html,body{width:1200px;height:900px;overflow:hidden;background:var(--page-bg)}
  .flyer{
    position:absolute;left:298px;top:20px;width:604px;height:860px;overflow:hidden;
    background:linear-gradient(180deg,var(--yellow) 0%,var(--orange) 70%,var(--yellow) 100%);
    font-family:"PT Sans",sans-serif;color:var(--panel-text);
    box-shadow:0 4px 18px rgba(0,0,0,.18);
  }
  .abs{position:absolute}
  .header-bar{left:0;top:0;width:100%;height:74px;background:var(--ink)}
  .header-title{left:14px;top:16px;font-family:"Bebas Neue",sans-serif;font-size:46px;font-weight:400;line-height:1;color:var(--white);letter-spacing:1px}
  .savings-band{left:0;top:74px;width:100%;height:56px;background:var(--white)}
  .savings-title{left:10px;top:80px;font-family:"Alfa Slab One",serif;font-size:36px;font-weight:400;line-height:1;color:var(--red);white-space:nowrap}
  .photo{display:block}
  .section-panel{background:linear-gradient(180deg,var(--yellow),var(--orange))}
  .section-head{font-family:"Bebas Neue",sans-serif;font-size:34px;line-height:1;color:var(--ink)}
  .section-copy{font-size:14px;line-height:1.18;color:var(--panel-text)}
  .section-head + .section-copy{margin-top:2px}
  .inline-head{font-family:"Bebas Neue",sans-serif;font-size:34px;color:var(--ink);line-height:1}
  .accessories{left:12px;top:496px;width:390px}
  .accessories .section-copy{font-size:13px;line-height:1.15}
  .contact-band{left:0;top:600px;width:100%;height:110px;background:linear-gradient(180deg,#fff8e6,var(--white))}
  .contact-lead,.contact-phone,.contact-email{font-family:"Arvo",serif;font-weight:700;line-height:1;white-space:nowrap}
  .contact-lead{left:70px;top:608px;font-size:29px;color:var(--red)}
  .contact-phone{left:150px;top:646px;font-size:30px;color:var(--ink)}
  .contact-email{left:84px;top:682px;font-size:23px;color:var(--ink)}
  .footer-band{left:0;top:740px;width:100%;height:120px;background:linear-gradient(180deg,var(--red),var(--red-deep))}
  .pay-methods{left:10px;top:812px;display:flex;flex-direction:column;gap:4px}
  .pay-name{display:flex;align-items:center;gap:5px;font-weight:700;font-size:13px;color:var(--white)}
  .pay-name::before{content:"";width:9px;height:9px;background:var(--white)}
  .terms{left:150px;top:806px;width:290px;font-size:11px;font-style:italic;line-height:1.15;color:var(--white)}
  .terms b{font-weight:700}
</style>
</head>
<body>
<main class="flyer">
  <div class="abs header-bar"></div>
  <h1 class="abs header-title">Partial Listing</h1>

  <div class="abs savings-band"></div>
  <svg class="abs photo" style="left:450px;top:74px" width="154" height="56" role="img" aria-label="Pendant ceiling lamps"><defs><linearGradient id="lampGrad" x1="0" y1="0" x2="0" y2="1"><stop offset="0" stop-color="#9a9a98"/><stop offset="1" stop-color="#f4f4f2"/></linearGradient></defs><rect width="154" height="56" fill="url(#lampGrad)"/></svg>
  <h2 class="abs savings-title">Load Up Huge Savings!</h2>

  <svg class="abs photo" style="left:0;top:130px" width="230" height="140" role="img" aria-label="Red lamp, black armchair and brown leather sofa"><defs><linearGradient id="livingGrad" x1="0" y1="0" x2="1" y2="1"><stop offset="0" stop-color="#f4f1ee"/><stop offset=".5" stop-color="#b84a3a"/><stop offset="1" stop-color="#4a2418"/></linearGradient></defs><rect width="230" height="140" fill="url(#livingGrad)"/></svg>
  <div class="abs section-panel" style="left:215px;top:144px;width:389px;height:124px;border-radius:14px 0 0 14px;padding:8px 14px 0 28px">
    <div class="section-copy"><span class="inline-head">Living Room</span> -choose from a large selection of leather and fabric sofas in traditional and contemporary designs, recliner sets, tufted back with carved wood trim, sectional and studded sets in a range of colors such as brown, black, forest, burgandy and safari</div>
  </div>

  <div class="abs section-panel" style="left:0;top:270px;width:458px;height:112px;padding:10px 10px 0 12px">
    <div class="section-copy"><span class="inline-head">Bedroom Suites</span> -classical sleigh beds, mission panel canopy beds in solid wood and veneers. Available in King size and Queen size. High quality King and Queen matress sets (Made in Canada) in single and double pillow tops</div>
  </div>
  <svg class="abs photo" style="left:458px;top:270px" width="146" height="112" role="img" aria-label="Cream sofa with red cushions"><defs><linearGradient id="bedGrad" x1="0" y1="0" x2="1" y2="1"><stop offset="0" stop-color="#ddd0bd"/><stop offset=".6" stop-color="#c8b79f"/><stop offset="1" stop-color="#a8412f"/></linearGradient></defs><rect width="146" height="112" fill="url(#bedGrad)"/></svg>

  <svg class="abs photo" style="left:0;top:382px" width="168" height="112" role="img" aria-label="Glass dining table with iron chairs"><defs><linearGradient id="diningGrad" x1="0" y1="0" x2="1" y2="1"><stop offset="0" stop-color="#9a8e7e"/><stop offset=".5" stop-color="#d9d3c9"/><stop offset="1" stop-color="#3e3a36"/></linearGradient></defs><rect width="168" height="112" fill="url(#diningGrad)"/></svg>
  <div class="abs section-panel" style="left:168px;top:382px;width:436px;height:112px;padding:8px 10px 0 14px">
    <div class="section-head">Dining Room and Kitchen Furniture</div>
    <div class="section-copy">3, 5, 6, 9 piece dinnette and pub sets in traditional and contemporary designs, dining room sets with matching buffets, and China cabinets in Mahogany, Walnut, Oak and Cherry.</div>
  </div>

  <div class="abs accessories">
    <div class="section-head">Accessories</div>
    <div class="section-copy">area rugs, grandfather clocks, oil paintings, television sets, stainless steel cookware, culinary sets, sofa tables, lamps, mirrors, coffee table sets, pedestals, ottomans, wineracks, benches, plant stands, etc.</div>
  </div>

  <div class="abs contact-band"></div>
  <div class="abs footer-band"></div>

  <svg class="abs photo" style="left:405px;top:496px" width="84" height="90" role="img" aria-label="White floral teapot"><defs><radialGradient id="potGrad"><stop offset="0" stop-color="#ffffff"/><stop offset="1" stop-color="#cfd6cc"/></radialGradient></defs><rect width="84" height="90" rx="10" fill="url(#potGrad)"/></svg>
  <svg class="abs photo" style="left:496px;top:488px" width="100" height="372" role="img" aria-label="Grandfather clock in red mahogany"><defs><linearGradient id="clockGrad" x1="0" y1="0" x2="1" y2="0"><stop offset="0" stop-color="#5a160c"/><stop offset=".5" stop-color="#9c3519"/><stop offset="1" stop-color="#4a1208"/></linearGradient></defs><rect width="100" height="372" fill="url(#clockGrad)"/></svg>

  <p class="abs contact-lead">For more information</p>
  <p class="abs contact-phone">905-555-0148</p>
  <p class="abs contact-email">info@brightlotsales.com</p>

  <svg class="abs photo" style="left:0;top:716px" width="488" height="86" role="img" aria-label="Armoire, chaise, side table, lounge chair, bench and recliner"><defs><linearGradient id="furnGrad" x1="0" y1="0" x2="1" y2="0"><stop offset="0" stop-color="#8a1c10"/><stop offset=".4" stop-color="#6b3a1e"/><stop offset=".7" stop-color="#e9e3d8"/><stop offset="1" stop-color="#1c1c1c"/></linearGradient></defs><rect width="488" height="86" fill="url(#furnGrad)" opacity=".9"/></svg>

  <div class="abs pay-methods">
    <span class="pay-name">Paylo</span>
    <span class="pay-name">Cardex</span>
  </div>
  <p class="abs terms"><b>Terms and Conditions:</b> Payment: Cash/ Paylo/ CX or Debit- 10% Buyers Premium. Products may differ from pictures shown and described. Items subject to additions and deletions. Additional terms and conditions as posted and announced.</p>
</main>
</body>
</html>
```